Build a Web page - Dovin Pratchell Homes, LLC - a custom home builder

We are a custom home builder in Wisconsin. Need a basic web page with a home page, About Us, Contact info, Gallery, and Testimonials page. Gallery will probably have sub-pages and each will have about ten pictures or less. I already own the domain and have web hosting through Wix, I just need the site built. Once the page is built I should be able to do the upkeep on it myself. If I need to add pictures or whatever.
Updates

Project Deadline Extended
Reason: I am still looking through designs and will select soon - thank you!

Target Market(s)

Gen X and Millennials who are looking to build a home. Custom built homes - not generic spec homes.

Industry/Entity Type

Home Builder

Number of Pages Required

5+ page

Font styles to use
Sans Serif

Colors
ffffff
ec1f27
000000
9d9d9d

Requirements
Must have
• I have no idea if I want coded or in coded. I'm not sure of the difference and why I would want one over the other.
Nice to have
• We like the following colors - red, black, gray, white.
Should not have
• not a big fan of clip art like hammers, tape measures, etc. Must look professional.

```html
<!DOCTYPE html>
<html lang="en">
<head>
<meta charset="utf-8">
<title>Dovin Pratchell Homes, LLC</title>
<link href="https://fonts.googleapis.com/css2?family=Raleway:wght@400;500;600;700&family=Open+Sans:ital,wght@0,400;0,600;0,700;1,400&display=swap" rel="stylesheet">
<style>
:root{
  --red:#b3242c;
  --red-bright:#c8262f;
  --red-deep:#8f1b22;
  --black:#151515;
  --ink:#222;
  --grey:#9d9d9d;
  --grey-text:#777;
  --panel:#efeded;
  --card:#ececec;
  --white:#fff;
}
*{box-sizing:border-box;margin:0;padding:0}
html,body{width:1200px;height:3600px;overflow:hidden;background:var(--white)}
body{position:relative;font-family:"Open Sans",Arial,sans-serif;color:var(--ink)}
.abs{position:absolute}
.heading{font-family:"Raleway",Arial,sans-serif;font-weight:500;font-size:36px;letter-spacing:1px;color:var(--ink)}
.center{left:0;width:1200px;text-align:center}
.rule{position:absolute;height:2px;background:#333;width:96px;left:552px}

/* header */
.site-header{left:0;top:0;width:1200px;height:96px;background:var(--white)}
.brand{left:91px;top:7px;width:150px;height:82px;display:flex;align-items:center;gap:10px}
.brand-square{width:22px;height:22px;background:var(--red)}
.brand-name{font-family:"Raleway",Arial,sans-serif;font-weight:700;font-size:15px;line-height:17px;color:var(--ink)}
.top-links{top:12px;left:770px;display:flex;align-items:center;gap:26px;font-size:13px;font-weight:600}
.top-links span{display:flex;align-items:center;gap:8px}
.nav{top:64px;left:340px;display:flex;font-size:12px;font-weight:600;letter-spacing:.5px}
.nav a{color:var(--ink);text-decoration:none;padding:0 35px;border-left:1px solid #ccc;line-height:20px}
.nav a:first-child{border-left:none}

/* hero */
.hero{left:0;top:96px;width:1200px;height:576px;background:linear-gradient(120deg,#3a2e26 0%,#6b5a4a 40%,#8a7866 55%,#4a3a2e 80%,#2a211b 100%)}
.hero-frame{left:370px;top:245px;width:283px;height:333px;border:3px solid var(--white)}
.hero-title{left:458px;top:290px;width:460px;font-family:"Raleway",Arial,sans-serif;font-weight:500;font-size:37px;line-height:48px;color:var(--white)}
.hero-text{left:458px;top:412px;width:460px;font-size:16px;line-height:26px;color:var(--white)}
.btn-red{background:var(--red);color:var(--white);font-size:16px;display:flex;align-items:center;justify-content:center}

/* about */
.about{left:0;top:684px;width:1200px;height:528px;background:var(--panel)}
.about-sub{left:84px;top:864px;width:480px;font-family:"Raleway",Arial,sans-serif;font-weight:500;font-size:18px;line-height:30px}
.about-text{left:84px;top:940px;width:490px;font-size:12.5px;line-height:24px;color:var(--grey-text)}
.btn-outline{border:2px solid var(--red);color:var(--ink);font-size:15px;display:flex;align-items:center;justify-content:center}
.photo{position:absolute}

/* testimonials */
.testimonials{left:0;top:2191px;width:1200px;height:425px;background:linear-gradient(180deg,var(--red) 0%,var(--red-bright) 100%)}
.quote-card{position:absolute;width:427px;height:105px;background:var(--card);padding:16px 20px;font-size:13px;line-height:24px;color:#333}
.quote-card::after{content:"";position:absolute;left:26px;bottom:-16px;border:16px solid transparent;border-top-color:var(--card);border-bottom:0}
.stars{position:absolute;right:20px;bottom:14px;color:var(--red);font-size:12px;letter-spacing:1px}
.avatar{position:absolute;width:58px;height:58px;border-radius:50%;background:#d8b9a0;border:2px solid var(--white)}
.client-name{position:absolute;color:var(--white);font-family:"Raleway",Arial,sans-serif;font-weight:700;font-size:16px}
.client-firm{position:absolute;color:#f1c9cb;font-size:13px;font-style:italic}
.slide-arrow{position:absolute;width:40px;height:40px;border:2px solid rgba(255,255,255,.7);border-radius:50%}

/* blog */
.post-box{position:absolute;background:var(--card);padding:24px 28px}
.post-title{font-family:"Raleway",Arial,sans-serif;font-weight:500;font-size:19px;margin-bottom:18px}
.post-text{font-size:12px;line-height:22px;color:var(--grey-text)}
.post-more{font-size:13px;color:var(--red);margin-top:12px}
.date-badge{position:absolute;width:68px;height:77px;background:var(--red);color:var(--white);text-align:center;font-family:"Raleway",Arial,sans-serif;font-size:20px;line-height:28px;padding-top:10px}

/* newsletter band */
.social-band{left:0;top:3163px;width:1200px;height:94px;background:var(--red)}
.social-dot{position:absolute;top:3198px;width:22px;height:22px;border-radius:50%;background:var(--white)}
.news-input{left:626px;top:3190px;width:358px;height:45px;background:#d0545a;color:#f3d0d2;font-size:12px;padding:14px 16px}
.news-btn{left:984px;top:3190px;width:127px;height:45px;background:var(--red-deep);color:var(--white);font-weight:700;font-size:15px;display:flex;align-items:center;justify-content:center}

/* footer */
.footer{left:0;top:3257px;width:1200px;height:295px;background:var(--black);color:#ddd}
.foot-brand{left:125px;top:3310px;width:190px;display:flex;align-items:center;gap:10px}
.foot-brand .brand-name{color:var(--white)}
.foot-col-title{position:absolute;top:3312px;font-size:13px;color:#ddd}
.foot-list{position:absolute;top:3358px;list-style:none;font-size:11px;font-weight:600;color:#ddd}
.foot-list li{height:31px;display:flex;align-items:center;gap:12px}
.foot-field{position:absolute;left:840px;width:204px;height:29px;border:1px solid #bbb;font-size:10px;color:#999;padding:7px 8px}
.foot-submit{left:840px;top:3494px;width:204px;height:27px;background:var(--red);color:var(--white);font-weight:700;font-size:13px;display:flex;align-items:center;justify-content:center}
.copyright{left:0;top:3552px;width:1200px;height:48px;background:#0c0c0c;color:#aaa;font-size:11px;text-align:center;line-height:48px}
</style>
</head>
<body>

<header class="abs site-header">
  <div class="abs brand"><div class="brand-square"></div><div class="brand-name">Dovin Pratchell<br>Homes, LLC</div></div>
  <div class="abs top-links">
    <span><svg width="18" height="16" viewBox="0 0 18 16" fill="none" stroke="#c8262f" stroke-width="2"><path d="M1 8h10M7 4l4 4-4 4M11 1h6v14h-6"/></svg>LOGIN</span>
    <span style="margin-left:-12px">REGISTER</span>
    <span style="margin-left:50px"><svg width="18" height="18" viewBox="0 0 18 18" fill="none" stroke="#c8262f" stroke-width="2"><path d="M3 2l4 1 1 4-2 1.5a10 10 0 0 0 4 4L11.5 10l4 1 1 4-2 1C8 16 2 10 2 4z"/></svg>844.555.0182</span>
  </div>
  <nav class="abs nav"><a>HOME</a><a>ABOUT US</a><a>GALLERY</a><a>TESTIMONIALS</a><a>CONTACT US</a></nav>
  <svg class="abs" style="left:1094px;top:64px" width="20" height="20" viewBox="0 0 20 20" fill="none" stroke="#333" stroke-width="2"><circle cx="8" cy="8" r="6"/><path d="M13 13l6 6"/></svg>
</header>

<section class="abs hero" role="img" aria-label="Photo of a warm living room with fireplace, bookshelves and leather armchairs"></section>
<div class="abs hero-frame"></div>
<h1 class="abs hero-title">LOREM IPSUM IS SIMPLY DUMMY TEXT</h1>
<p class="abs hero-text">It is a long established fact that a reader will be distracted by the readable content of a page when</p>
<div class="abs btn-red" style="left:610px;top:485px;width:146px;height:45px">Learn More</div>

<section class="abs about"></section>
<h2 class="abs heading" style="left:91px;top:776px">ABOUT US</h2>
<div class="abs" style="left:84px;top:828px;width:160px;height:2px;background:#333"></div>
<p class="abs about-sub">IS SIMPLY DUMMY TEXT OF THE PRINTING AND TYPESETTING INDUSTRY.</p>
<p class="abs about-text">It is a long established fact that a reader will be distracted by the readable content of a page when looking at its layout. The point of using Lorem Ipsum is that it has a more-or-less normal distribution of letters, as opposed to using 'Content here, content here', making it look like readable English. Many desktop publishing packages and web page editors now use Lorem Ipsum as their default model text, and a search for</p>
<div class="abs btn-outline" style="left:84px;top:1116px;width:146px;height:46px">LEARN MORE</div>
<div class="abs" style="left:746px;top:751px;width:368px;height:411px;background:var(--red)"></div>
<div class="photo" style="left:653px;top:804px;width:389px;height:305px;background:linear-gradient(180deg,#c9d4de 0%,#b9b0a2 45%,#6f8a4a 70%,#5d7a3a 100%)" role="img" aria-label="Photo of a single-storey home with front lawn and young tree"></div>

<h2 class="abs heading center" style="top:1282px">OUR GALLERY</h2>
<div class="rule" style="top:1334px"></div>
<div class="photo" style="left:86px;top:1370px;width:327px;height:348px;background:linear-gradient(160deg,#b8c6cc,#8a7a66 60%,#5e4e40)" role="img" aria-label="Photo of a family room with fireplace and ceiling fan"></div>
<div class="photo" style="left:437px;top:1370px;width:326px;height:161px;background:linear-gradient(160deg,#e3d2b0,#9b6a52 60%,#6a3a30)" role="img" aria-label="Photo of a living room with red armchairs"></div>
<div class="photo" style="left:787px;top:1370px;width:327px;height:161px;background:linear-gradient(160deg,#ece6da,#a46a40 60%,#6e4628)" role="img" aria-label="Photo of a wooden staircase"></div>
<div class="photo" style="left:437px;top:1555px;width:677px;height:163px;background:linear-gradient(180deg,#d6dde2 0%,#c8c0b2 40%,#8a7a64 75%,#6e7f48 100%)" role="img" aria-label="Photo of a backyard patio with fire pit and table"></div>
<div class="photo" style="left:86px;top:1742px;width:327px;height:161px;background:linear-gradient(180deg,#e0e4e2 0%,#8a4a3e 55%,#5f7e3e 100%)" role="img" aria-label="Photo of a red wooden deck on a lawn"></div>
<div class="photo" style="left:437px;top:1742px;width:326px;height:161px;background:linear-gradient(160deg,#9a6238,#c8b8a2 55%,#3a2a22)" role="img" aria-label="Photo of a kitchen with wood cabinets and island"></div>
<div class="photo" style="left:787px;top:1742px;width:327px;height:348px;background:linear-gradient(170deg,#e6e0d2,#a26a3e 45%,#7a4a2a 80%,#4a3226)" role="img" aria-label="Photo of a kitchen with breakfast bar and stools"></div>
<div class="photo" style="left:86px;top:1927px;width:677px;height:163px;background:linear-gradient(180deg,#b8cbe0 0%,#5e6e5a 45%,#8a8276 75%,#6e8a4a 100%)" role="img" aria-label="Photo of a two-storey house with three-car garage"></div>

<section class="abs testimonials" role="img" aria-label="Red-tinted city skyline backdrop"></section>
<h2 class="abs heading center" style="top:2248px;color:var(--white)">CLIENT'S TESTIMONIAL</h2>
<div class="rule" style="top:2298px;background:var(--white)"></div>
<div class="quote-card" style="left:149px;top:2369px">I would like to take this opportunity to say that the quality of service offered by SP has been highly impressive.I would like to take this opportunity to<span class="stars">★★★☆☆</span></div>
<div class="quote-card" style="left:629px;top:2369px">I would like to take this opportunity to say that the quality of service offered by SP has been highly impressive.I would like to take this opportunity to<span class="stars">★★★☆☆</span></div>
<div class="avatar" style="left:187px;top:2508px" role="img" aria-label="Client portrait"></div>
<div class="client-name" style="left:254px;top:2518px">Dara Whitfield</div>
<div class="client-firm" style="left:254px;top:2542px">Halvern LTD</div>
<div class="avatar" style="left:662px;top:2508px" role="img" aria-label="Client portrait"></div>
<div class="client-name" style="left:734px;top:2518px">Dara Whitfield</div>
<div class="client-firm" style="left:734px;top:2542px">Halvern LTD</div>
<svg class="slide-arrow" style="left:50px;top:2399px" viewBox="0 0 40 40" fill="none" stroke="#fff" stroke-width="2"><path d="M23 13l-7 7 7 7"/></svg>
<svg class="slide-arrow" style="left:1110px;top:2399px" viewBox="0 0 40 40" fill="none" stroke="#fff" stroke-width="2"><path d="M17 13l7 7-7 7"/></svg>

<h2 class="abs heading center" style="top:2683px">RECENT BLOG</h2>
<div class="rule" style="top:2734px"></div>
<div class="post-box" style="left:86px;top:2834px;width:240px;height:209px"><div class="post-title">Lorem ipsum dolor</div><div class="post-text">It is a long established fact that a reader will be distracted by the readable content of a page when looking at its layout.</div><div class="post-more">Read More...</div></div>
<div class="photo" style="left:326px;top:2801px;width:250px;height:271px;background:linear-gradient(180deg,#e2dccd 0%,#9a7a5a 40%,#a8322c 70%,#6a2a22 100%)" role="img" aria-label="Photo of a bedroom with patterned red bedspread"></div>
<div class="date-badge" style="left:326px;top:2801px">29<br>Nov</div>
<div class="post-box" style="left:626px;top:2834px;width:240px;height:209px"><div class="post-title">Lorem ipsum dolor</div><div class="post-text">It is a long established fact that a reader will be distracted by the readable content of a page when looking at its layout.</div><div class="post-more">Read More...</div></div>
<div class="photo" style="left:866px;top:2801px;width:248px;height:271px;background:linear-gradient(180deg,#5d9ad8 0%,#a8c8e6 35%,#7e8a74 60%,#5f8a3a 100%)" role="img" aria-label="Photo of a house exterior under blue sky"></div>
<div class="date-badge" style="left:866px;top:2801px">29<br>Nov</div>

<section class="abs social-band"></section>
<div class="social-dot" style="left:135px"></div>
<div class="social-dot" style="left:234px"></div>
<div class="social-dot" style="left:344px"></div>
<div class="social-dot" style="left:447px"></div>
<div class="abs news-input">Subscribe to our newsletter...</div>
<div class="abs news-btn">Subscribe</div>

<footer class="abs footer"></footer>
<div class="abs foot-brand"><div class="brand-square"></div><div class="brand-name">Dovin Pratchell<br>Homes, LLC</div></div>
<svg class="abs" style="left:90px;top:3422px" width="12" height="16" viewBox="0 0 12 16" fill="#c8262f"><path d="M6 0a6 6 0 0 1 6 6c0 4-6 10-6 10S0 10 0 6a6 6 0 0 1 6-6z"/><circle cx="6" cy="6" r="2" fill="#151515"/></svg>
<p class="abs" style="left:118px;top:3420px;width:170px;font-size:12px;line-height:17px;color:#ddd">It is a long established fact that a reader will be distracted by the</p>
<svg class="abs" style="left:90px;top:3488px" width="14" height="14" viewBox="0 0 18 18" fill="#c8262f"><path d="M3 1l4 1 1 4-2 1.5a10 10 0 0 0 4 4L11.5 10l4 1 1 4-2 2C7 17 1 11 1 3z"/></svg>
<p class="abs" style="left:118px;top:3486px;font-size:13px;font-weight:700;color:#ddd">514-555-0139</p>
<div class="foot-col-title" style="left:384px">Quick Links</div>
<ul class="foot-list" style="left:374px">
  <li><svg width="12" height="8" viewBox="0 0 12 8" fill="none" stroke="#ddd"><path d="M0 4h11M8 1l3 3-3 3"/></svg>HOME</li>
  <li><svg width="12" height="8" viewBox="0 0 12 8" fill="none" stroke="#ddd"><path d="M0 4h11M8 1l3 3-3 3"/></svg>ABOUT US</li>
  <li><svg width="12" height="8" viewBox="0 0 12 8" fill="none" stroke="#ddd"><path d="M0 4h11M8 1l3 3-3 3"/></svg>GALLERY</li>
  <li><svg width="12" height="8" viewBox="0 0 12 8" fill="none" stroke="#ddd"><path d="M0 4h11M8 1l3 3-3 3"/></svg>TESTIMONIALS</li>
  <li><svg width="12" height="8" viewBox="0 0 12 8" fill="none" stroke="#ddd"><path d="M0 4h11M8 1l3 3-3 3"/></svg>CONTACT US</li>
</ul>
<div class="foot-col-title" style="left:602px">Services</div>
<ul class="foot-list" style="left:602px">
  <li><svg width="12" height="8" viewBox="0 0 12 8" fill="none" stroke="#ddd"><path d="M0 4h11M8 1l3 3-3 3"/></svg>LOREM IPSUM</li>
  <li><svg width="12" height="8" viewBox="0 0 12 8" fill="none" stroke="#ddd"><path d="M0 4h11M8 1l3 3-3 3"/></svg>LOREM IPSUM</li>
  <li><svg width="12" height="8" viewBox="0 0 12 8" fill="none" stroke="#ddd"><path d="M0 4h11M8 1l3 3-3 3"/></svg>LOREM IPSUM</li>
  <li><svg width="12" height="8" viewBox="0 0 12 8" fill="none" stroke="#ddd"><path d="M0 4h11M8 1l3 3-3 3"/></svg>LOREM IPSUM</li>
</ul>
<div class="foot-col-title" style="left:840px">Contact Us</div>
<div class="foot-field" style="top:3360px">Name...</div>
<div class="foot-field" style="top:3403px">Email...</div>
<div class="foot-field" style="top:3446px">Phone No...</div>
<div class="abs foot-submit">SUBMIT</div>
<div class="abs copyright">dovinpratchellhomes.com2017 . All rights reserved</div>

</body>
</html>
```